MS Word and MS Powerpoint template creation using existing logo as style guide

Create a professional looking MS Word document template and MS powerpoint template for Corvant Advisory Pty Ltd using a logo that's already been created as the style guide. Corvant is a professional services business providing strategy, governance and execution support to small and medium business, Boards and executive teams. refer design brief.

Target Market(s)

Small to medium business, Chairs, Boards, executive teams, general managers

Industry/Entity Type

Professional business services, consultancy, business support outsourcing

Other font styles liked:
• calibri

Requirements
Must have
• leverage the existing logo for colour scheme. Use the CORVANT logo type font. Fully editable templates Word and MS Powerpoint,
Nice to have
• Refer to the design brief
Should not have
• animations, cartoons, stock images of people.

```html
<!DOCTYPE html>
<html lang="en">
<head>
<meta charset="utf-8">
<title>Corvant Advisory – Presentation Template</title>
<link href="https://fonts.googleapis.com/css2?family=Poppins:wght@400;500;600;700&display=swap" rel="stylesheet">
<style>
:root{
  --stage:#3a3b40;
  --navy:#1b3a57;
  --navy-deep:#143a5f;
  --blue:#2f5fa8;
  --blue-mid:#4a7fb8;
  --blue-soft:#8fb2d2;
  --sky:#5aa6e0;
  --paper:#f4f8fb;
  --mist:#dceaf4;
  --glow:#f2f0c8;
  --text:#1f3146;
}
*{margin:0;padding:0;box-sizing:border-box}
html,body{width:1200px;height:768px;overflow:hidden;background:var(--stage)}
body{position:relative;font-family:"Poppins",Arial,sans-serif;color:var(--text)}
.slide{
  position:absolute;width:521px;height:293px;overflow:hidden;
  background:
    radial-gradient(ellipse 70% 60% at 20% 95%, rgba(150,190,225,.55), transparent 70%),
    radial-gradient(ellipse 60% 50% at 95% 10%, rgba(190,215,235,.5), transparent 70%),
    linear-gradient(160deg,#fbfdff 0%,var(--paper) 45%,var(--mist) 100%);
  box-shadow:0 6px 16px rgba(0,0,0,.35);
}
.slide--cover{left:68px;top:80px}
.slide--agenda{left:611px;top:80px}
.slide--summary{left:68px;top:395px}
.slide--about{left:611px;top:395px}
.waves,.stripes,.photo{position:absolute;inset:0;width:521px;height:293px}
.brand{position:absolute;font-weight:500;color:var(--navy);letter-spacing:.14em;line-height:1}
.brand--lead{left:30px;top:36px;font-size:25px}
.brand--foot{left:37px;top:254px;font-size:16px}
.footer-rule{position:absolute;left:110px;top:272px;width:279px;height:0;border-top:.7px solid var(--navy)}
.url{position:absolute;font-weight:500;color:var(--navy);letter-spacing:.1em}
.url--foot{left:395px;top:263px;font-size:9.5px}
.url--cover{left:363px;top:254px;font-size:13px;color:var(--navy-deep)}
.cover-title{position:absolute;left:31px;top:134px;font-size:23.5px;font-weight:600;line-height:29px;color:var(--navy)}
.heading{position:absolute;font-weight:700;color:var(--navy);font-size:30px;line-height:30px;letter-spacing:.01em}
.agenda-list{position:absolute;left:49px;top:101px;list-style:none}
.agenda-list li{font-size:9.5px;line-height:16.6px;padding-left:14px;position:relative}
.agenda-list li::before{content:"";position:absolute;left:0;top:5px;width:5.5px;height:5.5px;background:var(--navy)}
.para{position:absolute;font-size:9.6px;line-height:11.4px;color:var(--text)}
.subhead{font-size:10px;font-weight:600;color:var(--navy)}
.about-copy{position:absolute;left:244px;top:113px;width:240px}
.about-copy p{font-size:9.5px;line-height:11.4px;margin-bottom:11px}
</style>
</head>
<body>

<!-- Cover -->
<section class="slide slide--cover">
  <svg class="waves" viewBox="0 0 521 293" aria-hidden="true">
    <path d="M0 150 C120 120 250 230 521 200" fill="none" stroke="var(--glow)" stroke-width="3" opacity=".8"/>
    <path d="M0 190 C150 140 260 280 521 240" fill="none" stroke="#ffffff" stroke-width="2" opacity=".8"/>
    <path d="M60 293 C120 200 260 140 521 120" fill="none" stroke="var(--glow)" stroke-width="2" opacity=".6"/>
  </svg>
  <svg class="stripes" viewBox="0 0 521 293" aria-hidden="true">
    <defs>
      <linearGradient id="coverFade" x1="0" y1="0" x2="0" y2="1">
        <stop offset="0" stop-color="var(--navy-deep)" stop-opacity=".95"/>
        <stop offset="1" stop-color="var(--blue-mid)" stop-opacity=".55"/>
      </linearGradient>
    </defs>
    <polygon points="400,0 430,0 250,293 220,293" fill="var(--blue-soft)" opacity=".55"/>
    <polygon points="445,0 521,0 521,40 318,293 270,293" fill="url(#coverFade)"/>
    <polygon points="505,95 521,95 521,110 360,293 342,293" fill="var(--blue)" opacity=".6"/>
  </svg>
  <div class="brand brand--lead">CORVANT</div>
  <h1 class="cover-title">Connecting<br>Strategy,<br>Governance &amp;<br>Execution</h1>
  <div class="url url--cover">www.corvant.com</div>
</section>

<!-- Agenda -->
<section class="slide slide--agenda">
  <svg class="waves" viewBox="0 0 521 293" aria-hidden="true">
    <path d="M0 230 C150 150 300 300 521 250" fill="none" stroke="var(--glow)" stroke-width="3" opacity=".8"/>
    <path d="M0 120 C100 90 200 200 400 180" fill="none" stroke="#ffffff" stroke-width="2" opacity=".7"/>
  </svg>
  <svg class="photo" viewBox="0 0 521 293" role="img" aria-label="Photograph of a hand touching a glowing network of connected people icons">
    <defs>
      <linearGradient id="netPhoto" x1="0" y1="0" x2="1" y2="1">
        <stop offset="0" stop-color="#9fb4c6"/>
        <stop offset=".5" stop-color="#6f8597"/>
        <stop offset="1" stop-color="#b9c6cf"/>
      </linearGradient>
    </defs>
    <polygon points="400,0 440,0 320,140 290,140" fill="var(--sky)" opacity=".55"/>
    <polygon points="442,0 521,0 521,252 244,252" fill="url(#netPhoto)"/>
  </svg>
  <h2 class="heading" style="left:39px;top:41px">AGENDA</h2>
  <ul class="agenda-list">
    <li>Context and background</li>
    <li>Problem / opportunity overview</li>
    <li>Objectives and success criteria</li>
    <li>Proposed approach</li>
    <li>Risks, governance and implications</li>
    <li>Decision sought</li>
  </ul>
  <div class="brand brand--foot">CORVANT</div>
  <div class="footer-rule"></div>
  <div class="url url--foot">www.corvant.com</div>
</section>

<!-- Executive summary -->
<section class="slide slide--summary">
  <svg class="waves" viewBox="0 0 521 293" aria-hidden="true">
    <path d="M0 140 C150 110 260 260 521 230" fill="none" stroke="var(--glow)" stroke-width="3" opacity=".8"/>
    <path d="M40 293 C140 200 300 190 521 150" fill="none" stroke="#ffffff" stroke-width="2" opacity=".7"/>
  </svg>
  <svg class="stripes" viewBox="0 0 521 293" aria-hidden="true">
    <polygon points="455,0 475,0 370,145 350,145" fill="var(--blue-soft)" opacity=".5"/>
    <polygon points="488,0 521,0 521,30 440,143 408,143" fill="var(--navy-deep)" opacity=".85"/>
    <polygon points="515,40 521,40 521,52 450,143 442,143" fill="var(--blue)" opacity=".6"/>
  </svg>
  <h2 class="heading" style="left:39px;top:39px">EXECUTIVE<br>SUMMARY</h2>
  <p class="para" style="left:48px;top:155px;width:175px">This paper outlines the current context, identifies key challenges and opportunities, and presents a recommended course of action for consideration by the Board.</p>
  <p class="para" style="left:261px;top:155px;width:175px">The proposed approach is aligned to strategic priorities, governance requirements, and execution capability, ensuring decisions are both sound and deliverable.</p>
  <div class="brand brand--foot">CORVANT</div>
  <div class="footer-rule"></div>
  <div class="url url--foot">www.corvant.com</div>
</section>

<!-- About us -->
<section class="slide slide--about">
  <svg class="waves" viewBox="0 0 521 293" aria-hidden="true">
    <path d="M0 200 C150 170 300 300 521 240" fill="none" stroke="var(--glow)" stroke-width="3" opacity=".8"/>
    <path d="M100 293 C200 210 350 200 521 170" fill="none" stroke="#ffffff" stroke-width="2" opacity=".7"/>
  </svg>
  <svg class="photo" viewBox="0 0 521 293" role="img" aria-label="Photograph of a fountain pen resting on printed documents on a desk">
    <defs>
      <linearGradient id="deskPhoto" x1="0" y1="0" x2="0" y2="1">
        <stop offset="0" stop-color="#5d7fb8"/>
        <stop offset=".5" stop-color="#8fb0e0"/>
        <stop offset="1" stop-color="#c9daf0"/>
      </linearGradient>
    </defs>
    <polygon points="0,0 247,0 140,140 185,200 120,218 0,218" fill="url(#deskPhoto)"/>
    <polygon points="220,0 247,0 140,140 125,125" fill="var(--sky)" opacity=".7"/>
  </svg>
  <h2 class="heading" style="left:244px;top:56px">ABOUT US</h2>
  <div class="about-copy">
    <p><span class="subhead">Who We Are</span><br>CORVANT Management is a professional advisory firm providing strategy, governance, and execution support to Boards and executive leadership teams.</p>
    <p><span class="subhead">Our Role</span><br>We work alongside decision-makers to bring structure, clarity, and accountability to complex initiatives.</p>
  </div>
  <div class="brand brand--foot">CORVANT</div>
  <div class="footer-rule"></div>
  <div class="url url--foot">www.corvant.com</div>
</section>

</body>
</html>
```